Partnership Enterprise Architects looking for Business Flyer (Dutch laguage)

We are a partnership of independent IT Architects working in various roles within our clients (Goverment agencies, Financial institutions and for profit companies). With this flyer we would like to promote ourselves in a inviting but still business like way. We would like to see our logo and name (Maatschap Veltrix) and the graphs and text we used in our example as the basis of the flyer. Anything else is up to your creativity. Colors and 'look and feel' of the graphs may be altered as long as the text (Dutch language remains unchanged). We think a 2 page A4 format flyer would serve best, but are open to suggestions.

Target Market(s)

Clients in the field of Government agencies, Financial institutions and for profit comapnies as well as possible future partners in the ICT Architect field

Industry/Entity Type

Business

Font styles to use
Sans Serif
Other font styles liked:
• Calibri 11 is our standard font

Colors

Designer to choose colors to be used in the design.

Requirements
Must have
• The text (verbatim in the Dutch laguage) as well as the graphs (they may be altered as you see fit as long as the general point and meaning remain the same). Logo preferably upper right corner. 2 A4 double sided flyer in one piece (

```html
<!DOCTYPE html>
<html lang="nl">
<head>
<meta charset="utf-8">
<title>Maatschap Veltrix – Flyer</title>
<link href="https://fonts.googleapis.com/css2?family=Montserrat:wght@700;800&family=Oswald:wght@700&family=Lato:wght@400;700&display=swap" rel="stylesheet">
<style>
  :root{
    --canvas:#d9d9d9;
    --ink:#1a1a1a;
    --black:#141414;
    --red:#e30613;
    --white:#ffffff;
    --sky:#8db2d6;
    --haze:#f4f1e4;
    --panel-top:#dcdcdc;
    --panel-bottom:#f7f7f7;
    --photo-grey:#8a8a8a;
  }
  *{box-sizing:border-box;margin:0;padding:0}
  html,body{width:1200px;height:1200px;overflow:hidden;background:var(--canvas)}
  .flyer{position:absolute;left:175px;top:0;width:850px;height:1200px;background:var(--white);overflow:hidden;font-family:"Lato",sans-serif;color:var(--ink)}
  .hero{position:absolute;left:0;top:0;width:850px;height:660px;
    background:
      radial-gradient(ellipse 260px 220px at 180px 170px,rgba(255,255,255,1),rgba(255,255,255,0) 70%),
      radial-gradient(circle 90px at 520px 420px,rgba(255,250,225,.95),rgba(255,250,225,0)),
      linear-gradient(180deg,var(--sky) 0%,#c9dbe9 35%,var(--haze) 55%,#5a5650 70%,#1c1c1c 85%,var(--black) 100%);}
  .brand{position:absolute;left:30px;top:70px;display:flex;align-items:center;gap:10px}
  .brand-mark{width:22px;height:22px;background:var(--ink)}
  .brand-name{font-family:"Lato",sans-serif;font-weight:700;font-size:30px;line-height:30px;color:var(--ink)}
  .tag{position:absolute;left:0;display:flex;align-items:center;padding-left:24px}
  .tag-dark{background:var(--black);color:var(--white);font-family:"Montserrat",sans-serif;font-weight:800;font-size:27px;letter-spacing:.5px}
  .tag-light{background:var(--white);color:var(--red);font-family:"Oswald",sans-serif;font-weight:700;font-size:36px;letter-spacing:-.5px}
  .tag-1{top:514px;width:291px;height:36px}
  .tag-2{top:556px;width:497px;height:38px}
  .tag-3{top:599px;width:596px;height:36px}
  .section-title{font-family:"Montserrat",sans-serif;font-weight:700;font-size:15.5px;color:var(--red);letter-spacing:.4px;text-transform:uppercase}
  .body{font-size:11.6px;line-height:14.9px}
  .photo{position:absolute;background:linear-gradient(180deg,#5e5e5e,var(--photo-grey) 40%,#6a6a6a)}
  .sign{position:absolute;background:#f2f2f2;font-family:"Courier New",monospace;font-weight:700;color:var(--ink);text-align:center}
  .intro{position:absolute;left:0;top:660px;width:850px;height:139px}
  .intro .photo{left:24px;top:0;width:154px;height:139px}
  .intro .sign{left:28px;top:22px;width:108px;height:108px;font-size:11.5px;line-height:19px;padding-top:6px}
  .intro .text{position:absolute;left:210px;top:6px;width:622px}
  .intro .section-title{margin-bottom:2px}
  .rule{position:absolute;left:0;width:850px;height:4px;background:var(--black)}
  .rule-1{top:799px}
  .rule-2{top:945px}
  .method{position:absolute;left:0;top:809px;width:850px;height:136px}
  .method .text{position:absolute;left:24px;top:6px;width:628px}
  .method .section-title{margin-bottom:5px}
  .method .photo{left:669px;top:9px;width:155px;height:127px}
  .method .sign{left:30px;top:22px;width:100px;height:100px;font-family:"Lato",sans-serif;font-size:12px;line-height:15px;padding-top:10px}
  .offer{position:absolute;left:0;top:949px;width:850px;height:221px;background:linear-gradient(180deg,var(--panel-top),var(--panel-bottom) 45%,var(--white))}
  .col{position:absolute;top:38px}
  .col-left{left:31px;width:380px}
  .col-right{left:432px;width:370px}
  .col .section-title{margin-bottom:8px}
  .col p{margin-bottom:4px}
  .bullets{list-style:none}
  .bullets li{position:relative;padding-left:15px}
  .bullets li::before{content:"";position:absolute;left:2px;top:5px;width:5px;height:5px;border-radius:50%;background:var(--red)}
  .bullet-pair{display:flex}
  .bullet-pair ul:first-child{width:200px}
  .footer-band{position:absolute;left:0;top:1170px;width:850px;height:30px;background:var(--red)}
</style>
</head>
<body>
<main class="flyer">
  <section class="hero" role="img" aria-label="Foto: silhouet van een persoon met een vlag op een bergtop tegen een zonnige, blauwe lucht">
    <div class="brand">
      <div class="brand-mark"></div>
      <div class="brand-name">Nova Kring Groep</div>
    </div>
  </section>
  <div class="tag tag-dark tag-1">HET GROOTSTE</div>
  <div class="tag tag-light tag-2">FYSIEKE ICT EXPERTISENETWERK</div>
  <div class="tag tag-dark tag-3">VAN ONDERNEMERS IN NEDERLAND</div>

  <section class="intro">
    <div class="photo" role="img" aria-label="Foto: persoon houdt een bord vast met de tekst 'De klantvraag staat centraal ALTIJD'">
      <div class="sign">De klantvraag<br>staat centraal<br><br>ALTIJD</div>
    </div>
    <div class="text">
      <h2 class="section-title">Maatschap Veltrix</h2>
      <p class="body">De maten vormen een collectief van initiatiefrijke, ervaren (15 jaar of meer) en gedreven zelfstandige ondernemers. We vinden dat de bedrijfsvraagstukken leidend zijn. IT-producten en -pakketten, architectuur, methoden en technieken zijn hulpmiddelen en geen doelen op zich.<br>
      Het ondersteunen van de opdrachtgever bij het demand-vraagstuk en het stellen van de goede vraag aan de IT-leverende partij, staat bij ons centraal.<br>
      We zijn zelfstandig ondernemers zonder binding aan een product of methode. We zijn een verrijking, geen beperking van uw organisatie en we voeren uw agenda uit.</p>
    </div>
  </section>
  <div class="rule rule-1"></div>

  <section class="method">
    <div class="text">
      <h2 class="section-title">Hoe we werken</h2>
      <p class="body">We helpen de beslisser beslissen. Dit doen we door de business eisen en wensen helder te maken en die te vertalen in (business en IT) oplossingen. Het vormen van oplossingen doen we door het toepassen van, door de jaren heen, bij andere klanten opgebouwde best practices.<br>
      Elk van onze ondernemers wordt ondersteund door een omvangrijk kennisnetwerk. We wisselen ervaringen uit en bouwen actief aan onze vakkennis. Op die manier garanderen we dat onze kennis up-to-date is en relevant blijft.<br>
      De maatschap levert een onder de door de Rijksfiscus goedgekeurde modelovereenkomst.</p>
    </div>
    <div class="photo" role="img" aria-label="Foto: persoon houdt een bord vast met de tekst 'Belangrijke beslissingen aanpakken met architectuur'">
      <div class="sign">Belangrijke<br>beslissingen<br>aanpakken<br>met<br>architectuur</div>
    </div>
  </section>
  <div class="rule rule-2"></div>

  <section class="offer">
    <div class="col col-left">
      <h2 class="section-title">Wat we bieden</h2>
      <p class="body">Een greep uit de bedrijfs- en IT-vraagstukken waarbij we helpen:</p>
      <ul class="bullets body">
        <li>IT strategie;</li>
        <li>Procesinrichting en -harmonisatie;</li>
        <li>Portfolio management;</li>
        <li>Inrichten van governance;</li>
        <li>Business - IT alignment, IT transformatie;</li>
        <li>Innovatie en vernieuwing;</li>
        <li>Scenario analyse.</li>
        <li>Daarnaast bieden we architectuurtraining, -opleiding en -coaching.</li>
      </ul>
    </div>
    <div class="col col-right">
      <h2 class="section-title">Wat we bieden</h2>
      <p class="body">De maten hebben werkervaring in overheid, zorg, onderwijs, transport, telecom, media, financiële dienstverlening, verzekeringen en nutsbedrijven.<br>
      De maten zijn gecertificeerd voor gangbare methoden en industrie standaarden:</p>
      <div class="bullet-pair body">
        <ul class="bullets">
          <li>KPX en Flow Kwaliteit;</li>
          <li>KAF, VRA, ORBIS en NEA;</li>
          <li>Modelmaat;</li>
        </ul>
        <ul class="bullets">
          <li>SPRINTA en FLOWR;</li>
          <li>BIBO/ASO/DIVO;</li>
          <li>EVRA.</li>
        </ul>
      </div>
    </div>
  </section>
  <div class="footer-band"></div>
</main>
</body>
</html>
```